Looking to design a new sign for our church.

Looking for a new sign
4 x 8 feet dimension
We are renaming the church "Medlow Ridge Community Church"
looking for legible graphics
Would like some type of backdrop being a family tree (oak) / open to other ideas as you are led
I have included a pic of the old sign for your review
would like to incorporate our Hillside Missions on the lower right hand corner of the sign / see file attached

```html
<!DOCTYPE html>
<html lang="en">
<head>
<meta charset="utf-8">
<title>Medlow Ridge Community Church – Sign</title>
<link rel="stylesheet" href="https://fonts.googleapis.com/css2?family=Barlow+Semi+Condensed:wght@600;700&family=Nunito:wght@700&family=Carlito&display=swap">
<style>
  :root {
    --page: #eeeae6;
    --sign-face: #fcd7c9;
    --maroon: #5b1718;
    --ink: #111111;
  }
  * { margin: 0; padding: 0; box-sizing: border-box; }
  html, body { width: 837px; height: 1200px; overflow: hidden; }
  body { background: var(--page); position: relative; }

  .sign {
    position: absolute;
    left: 45px;
    top: 414px;
    width: 747px;
    height: 372px;
    background: var(--sign-face);
    border: 4px solid var(--maroon);
  }
  .sign-title {
    position: absolute;
    left: 0; right: 0;
    top: 40px;
    text-align: center;
    font-family: "Barlow Semi Condensed", sans-serif;
    font-weight: 700;
    font-size: 168px;
    line-height: 1;
    letter-spacing: 2px;
    color: var(--maroon);
  }
  .sign-subtitle {
    position: absolute;
    left: 0; right: 0;
    top: 204px;
    text-align: center;
    font-family: "Barlow Semi Condensed", sans-serif;
    font-weight: 600;
    font-size: 54px;
    line-height: 1;
    letter-spacing: 1px;
    color: var(--ink);
  }
  .sign-rule {
    position: absolute;
    left: 56px;
    right: 8px;
    top: 290px;
    height: 2px;
    background: var(--maroon);
  }
  .schedule {
    position: absolute;
    left: 86px;
    right: 16px;
    top: 306px;
    display: flex;
    justify-content: space-between;
  }
  .service { text-align: center; }
  .service-time {
    display: block;
    font-family: "Nunito", sans-serif;
    font-weight: 700;
    font-size: 24px;
    line-height: 1.1;
    color: var(--maroon);
  }
  .service-name {
    display: block;
    font-family: "Carlito", sans-serif;
    font-size: 26px;
    line-height: 1.05;
    color: var(--ink);
  }
  .ministry-mark {
    position: absolute;
    left: 10px;
    top: 292px;
    width: 44px;
    text-align: center;
    font-family: "Carlito", sans-serif;
    font-size: 8px;
    line-height: 1.1;
    color: var(--maroon);
  }
  .ministry-mark svg { display: block; margin: 0 auto 4px; }
</style>
</head>
<body>
  <div class="sign">
    <div class="sign-title">MEDLOW</div>
    <div class="sign-subtitle">RIDGE COMMUNITY CHURCH</div>
    <div class="sign-rule"></div>

    <div class="ministry-mark">
      <svg width="22" height="22" viewBox="0 0 22 22" aria-hidden="true">
        <circle cx="11" cy="11" r="10" fill="var(--maroon)"/>
      </svg>
      Hillside<br>Missions
    </div>

    <div class="schedule">
      <div class="service">
        <span class="service-time">10:30 am</span>
        <span class="service-name">Worship Service</span>
      </div>
      <div class="service">
        <span class="service-time">9:30 am</span>
        <span class="service-name">Sunday School</span>
      </div>
      <div class="service">
        <span class="service-time">6:00 pm</span>
        <span class="service-name">Wednesday Service</span>
      </div>
    </div>
  </div>
</body>
</html>
```